PAcifier/dummy design

Brand - Fable & Fern
Company - Australian designed ethical quality natural range.
Product - natural rubber soother/pacifier/dummy.
Box - 2 dummy's per box.
- hangable in store and stackable on shelf.
- box created with POS stand in mind would be amazing.
- box that is compact and easily ship-able.
- ideas - milk carton - or flat top milk carton style...
- matte finish.
Feel - modern, organic, boutique, clean and simplistic.
Natural product but for the boutique buyer, but can alos be placed in upmarket chemist, quality health food shop or chain store. target is not the hippy natural style, but the modern mama after something clean and quality.
for example - the mum from this page may buy it - https://www.instagram.com/pebbleandlark/
Colours & tones - matte finish.
- black logo
- white, cardboard tone, and soft tones included in the wreath in the images.
- current packaging image included.
Vision - designed in australia - made in Malaysia - exported to the world
Product variations
There are products that are the same but the brand sets them apart....
for example -
Breast feeding biscuits
A = cheap look https://www.instagram.com/mumcrumbsco/
B = quality look https://www.instagram.com/velmaspantry/
Lipgloss
A = cheap https://www.instagram.com/glintara_beauty/
B = quality https://www.instagram.com/dewbycorvell/
Boxes included - kanagroo - I had originally wanted an animal - i have decided to just get a beautiful packaging. simple, modern and lovely. I do like the font used in the kanagroo box tho
The other packaging designs are examples of what I thought - but the tall box will be hard to ship.
Target Market(s)
Baby - Organic natural modern mumma
Stores - premium pharmacies, baby boutiques. Department stores.

```html
<!DOCTYPE html>
<html lang="en">
<head>
<meta charset="utf-8">
<title>Fable &amp; Fern — Natural Rubber Pacifier Box Dieline</title>
<link rel="stylesheet" href="https://fonts.googleapis.com/css2?family=Libre+Baskerville:wght@400;700&display=swap">
<style>
  :root {
    --board: #b9974a;
    --fold: #ffffff;
    --ink: #1a1a1a;
    --badge-gold: #cfa42f;
    --badge-rust: #c96f2b;
    --art-warm: #c8702a;
    --art-sand: #d9c192;
    --hole-edge: #9a9a9a;
    --page: #ffffff;
  }
  html, body {
    margin: 0;
    padding: 0;
    width: 1133px;
    height: 1200px;
    overflow: hidden;
    background: var(--page);
  }
  .canvas {
    position: relative;
    width: 1133px;
    height: 1200px;
  }
  .dieline {
    position: absolute;
    left: 110px;
    top: 238px;
    width: 913px;
    height: 723px;
  }
  .panel { fill: var(--board); }
  .fold-line { stroke: var(--fold); stroke-width: 1; fill: none; }
  .hang-hole { fill: var(--page); stroke: var(--hole-edge); stroke-width: 1.5; }
  .type { font-family: "Libre Baskerville", "Baskerville", serif; fill: var(--ink); }
  .brand-name { font-size: 15px; letter-spacing: 0.5px; }
  .sub-line { font-size: 7.5px; letter-spacing: 0.2px; }
  .product-line { font-size: 11.5px; font-weight: 700; letter-spacing: 2px; }
  .product-name { font-size: 13.5px; letter-spacing: 1.6px; }
  .tagline { font-size: 6.2px; }
  .age-num { font-size: 13px; font-weight: 700; }
  .age-unit { font-size: 5.5px; }
  .twin-text { font-size: 8px; fill: #fff; letter-spacing: 1.5px; }
  .age-badge { fill: var(--badge-gold); }
  .twin-badge { fill: var(--badge-rust); }
  .art-window { fill: #ffffff; }
  .art-frame { fill: none; stroke: #000; stroke-width: 5; }
</style>
</head>
<body>
<main class="canvas">
  <svg class="dieline" viewBox="239 652 702 556" xmlns="http://www.w3.org/2000/svg">
    <defs>
      <linearGradient id="art-tones" x1="0" y1="0" x2="0" y2="1">
        <stop offset="0" stop-color="#d9c192"/>
        <stop offset="1" stop-color="#c8702a"/>
      </linearGradient>
    </defs>

    <!-- panels -->
    <rect class="panel front-hanger" x="377" y="652" width="213" height="92"/>
    <rect class="panel back-hanger" x="729" y="652" width="212" height="92"/>
    <rect class="panel left-side" x="239" y="744" width="138" height="324"/>
    <rect class="panel front" x="377" y="744" width="213" height="324"/>
    <rect class="panel right-side" x="590" y="744" width="139" height="324"/>
    <rect class="panel back" x="729" y="744" width="212" height="324"/>
    <rect class="panel bottom-flap" x="377" y="1068" width="213" height="140"/>

    <!-- fold lines -->
    <line class="fold-line" x1="239" y1="744" x2="941" y2="744"/>
    <line class="fold-line" x1="377" y1="744" x2="377" y2="1068"/>
    <line class="fold-line" x1="590" y1="744" x2="590" y2="1068"/>
    <line class="fold-line" x1="729" y1="744" x2="729" y2="1068"/>
    <line class="fold-line" x1="377" y1="1068" x2="590" y2="1068"/>
    <polyline class="fold-line" points="308,744 308,997"/>
    <polyline class="fold-line" points="239,1068 308,997 377,1068"/>
    <polyline class="fold-line" points="660,744 660,997"/>
    <polyline class="fold-line" points="590,1068 660,997 729,1068"/>

    <!-- front hanger -->
    <circle class="age-badge" cx="411" cy="698" r="18"/>
    <text class="type age-num" x="411" y="700" text-anchor="middle">6|8</text>
    <text class="type age-unit" x="411" y="709" text-anchor="middle">monts</text>
    <ellipse class="hang-hole" cx="483" cy="698" rx="10" ry="15"/>
    <rect class="twin-badge" x="530" y="681" width="45" height="35" rx="5"/>
    <text class="type twin-text" x="552.5" y="695" text-anchor="middle">TWIN</text>
    <text class="type twin-text" x="552.5" y="708" text-anchor="middle">PACK</text>

    <!-- back hanger -->
    <ellipse class="hang-hole" cx="835" cy="698" rx="10" ry="15"/>

    <!-- front panel -->
    <text class="type brand-name" x="483" y="795" text-anchor="middle">Fable &amp; Fern</text>
    <text class="type sub-line" x="481" y="820" text-anchor="middle">NATURAL RUBBER</text>
    <text class="type product-line" x="481" y="835" text-anchor="middle">PACIFIER</text>

    <rect class="art-window" x="424" y="867" width="119" height="139"/>
    <rect class="art-illustration" x="440" y="842" width="87" height="162" fill="url(#art-tones)" role="img" aria-label="Illustration of a kangaroo joey peeking out of a framed window"/>
    <rect class="art-frame" x="424" y="867" width="119" height="139"/>

    <text class="type product-name" x="484" y="1040" text-anchor="middle">wren soother</text>
    <text class="type tagline" x="483" y="1055" text-anchor="middle">with an organic bamboo carry pouch</text>
  </svg>
</main>
</body>
</html>
```